Organic Soap Packaging

We need a package design for a new company called Willow Naturals. Our primary product is organic soap. Our business model is based on the social entrepreneurial concept of by one give one like Brend shoes. We are giving soap to help prevent the spread of disease; 1.4 million deaths a year can be prevented by hand washing.

The design is for a recycled cardboard box/package. We want to demonstrate the high end, luxury feel of the product with undertones of organic/earth friendly/social conscious.

The soap is small batch, spa like, essential oil scented all natural luxury.
Updates

I am very excited about this startup business and I believe we will have great success! I am passionate about organic personal care and helping others in need. If you share my passion, please bring your work to the table!

Target Market(s)

My target market is people who are educated through college. Health conscious, socially conscious, Generation X. Basically shoppers of Green Basket and Haverline.

Industry/Entity Type

Business

Requirements
Must have
• Suitable for Face, Hair, and Skin
Scented with Organic Essential Oils

```html
<!DOCTYPE html>
<html lang="en">
<head>
<meta charset="utf-8">
<title>Willow Naturals — Organic Soap Box</title>
<link rel="stylesheet" href="https://fonts.googleapis.com/css2?family=Bodoni+Moda:wght@400;500&display=swap">
<style>
  :root {
    --page-bg: #ffffff;
    --kraft: #bcab8f;
    --kraft-edge: #ad9b7e;
    --label-bg: #f9fbf4;
    --label-tint: #eef4e2;
    --rule-green: #7f8f45;
    --brand-green: #6e7e38;
    --ink-grey: #555656;
    --leaf-dark: #1f3d0c;
    --leaf-mid: #4f8a16;
    --leaf-bright: #9fd42a;
  }
  * { margin: 0; padding: 0; box-sizing: border-box; }
  html, body {
    width: 1200px;
    height: 1000px;
    overflow: hidden;
    background: var(--page-bg);
  }
  body { position: relative; font-family: "Bodoni Moda", "Didot", serif; }

  .box-front {
    position: absolute;
    left: 216px;
    top: 199px;
    width: 782px;
    height: 568px;
    background: var(--kraft);
    border-radius: 3px;
    box-shadow: inset 0 0 0 1px var(--kraft-edge);
  }

  .sleeve {
    position: absolute;
    left: 121px;
    top: 0;
    width: 546px;
    height: 568px;
  }

  .leaf-band {
    position: absolute;
    left: 0;
    width: 100%;
  }
  .leaf-band--top {
    top: 0;
    height: 63px;
    background: linear-gradient(100deg, var(--leaf-dark) 0%, var(--leaf-mid) 22%, var(--leaf-bright) 40%, var(--leaf-mid) 55%, var(--leaf-dark) 70%, var(--leaf-mid) 85%, var(--leaf-dark) 100%);
  }
  .leaf-band--bottom {
    bottom: 0;
    height: 70px;
    background: linear-gradient(80deg, var(--leaf-dark) 0%, var(--leaf-mid) 20%, var(--leaf-bright) 38%, var(--leaf-mid) 52%, var(--leaf-bright) 65%, var(--leaf-dark) 85%, var(--leaf-dark) 100%);
  }

  .label {
    position: absolute;
    left: 0;
    top: 63px;
    width: 100%;
    height: 435px;
    background: radial-gradient(ellipse at 50% 50%, var(--label-bg) 0%, var(--label-tint) 100%);
    text-align: center;
  }
  .label__edge {
    position: absolute;
    left: 0;
    width: 100%;
    height: 2px;
    background: var(--rule-green);
    opacity: 0.7;
  }
  .label__edge--top { top: 5px; }
  .label__edge--bottom { bottom: 5px; }

  .brand {
    position: absolute;
    top: 74px;
    left: 0;
    width: 100%;
    display: flex;
    justify-content: center;
    align-items: center;
    gap: 12px;
  }
  .brand__mark {
    width: 22px;
    height: 22px;
    background: var(--brand-green);
  }
  .brand__name {
    font-size: 30px;
    font-weight: 500;
    color: var(--brand-green);
    letter-spacing: 0.5px;
  }

  .product-title {
    position: absolute;
    top: 161px;
    left: 41px;
    width: 469px;
    height: 66px;
    border-top: 2px solid var(--rule-green);
    border-bottom: 2px solid var(--rule-green);
    font-size: 63px;
    font-weight: 400;
    line-height: 62px;
    color: var(--ink-grey);
    white-space: nowrap;
    letter-spacing: -0.5px;
  }
  .product-title__accent { color: var(--brand-green); }

  .claim {
    position: absolute;
    top: 279px;
    left: 0;
    width: 100%;
    font-size: 23px;
    color: var(--ink-grey);
  }
  .scent-note {
    position: absolute;
    top: 330px;
    left: 0;
    width: 100%;
    font-size: 18px;
    line-height: 23px;
    color: var(--brand-green);
  }
</style>
</head>
<body>
  <div class="box-front">
    <div class="sleeve">
      <div class="leaf-band leaf-band--top" role="img" aria-label="Close-up photograph of bright green leaves"></div>

      <section class="label">
        <div class="label__edge label__edge--top"></div>

        <div class="brand">
          <span class="brand__mark"></span>
          <span class="brand__name">Willow Naturals</span>
        </div>

        <h1 class="product-title">ORGANIC <span class="product-title__accent">SOAP</span></h1>

        <p class="claim">Suitable for Face, Hair &amp; Skin</p>
        <p class="scent-note">Scented with<br>Organic Essential Oils</p>

        <div class="label__edge label__edge--bottom"></div>
      </section>

      <div class="leaf-band leaf-band--bottom" role="img" aria-label="Close-up photograph of bright green leaves"></div>
    </div>
  </div>
</body>
</html>
```